Dry mango packing design

Brand name : Orchard nibble
Product : Dry mango extra low sugar ( for healthy )
Position of product : Snack for healthy

Theme : Yellow , Green ,brown , Gold and you can put other color but not more than main theme color.

Over all must look for healthy , This is extra low sugar mango for healthy

Size : 6 x 9 inc

Must have :
-Picture of Yellow mango
-GMP logo

What we need you make :
1. Make new style of Brand name : Orchard nibble
2. Create new style , layout of packing bag of orchard nibble dry mango. front and back
3. At the front need transparent window. to show the real product.
4. Nutrition detail follow our old packaging ( File name : mango 5x8 copy2222222.jpg Check i a file )
5. Over all must look for healthy , This is extra low sugar mango for healthy

any question can contact me
miloqr382

***A picture that does not infringe copyright.***
Available to any idea welcome.

```html
<!DOCTYPE html>
<html lang="en">
<head>
<meta charset="utf-8">
<title>Orchard nibble Dried Mango – Pouch Front and Back</title>
<link href="https://fonts.googleapis.com/css2?family=Bitter:wght@600;800&family=Cabin:wght@400;600;700&display=swap" rel="stylesheet">
<style>
  :root{
    --stage:#8d8580;
    --orange:#f0961c;
    --orange-deep:#d9780e;
    --orange-light:#f8b445;
    --brown:#4a2a12;
    --brown-mid:#6b3d18;
    --slate:#4d4c4a;
    --slate-dark:#3a3937;
    --gold:#f6b21b;
    --cream:#fff3c4;
    --paper:#ffffff;
    --ink:#222;
    --gmp:#2f8a34;
    --badge:#b3201c;
  }
  html,body{margin:0;padding:0;overflow:hidden}
  body{width:1200px;height:900px;background:var(--stage);position:relative;font-family:"Cabin",sans-serif}
  .pouch{position:absolute;overflow:hidden;border-radius:6px;
    background:linear-gradient(180deg,var(--orange-light) 0%,var(--orange) 45%,var(--orange-deep) 100%)}
  .pouch-front{left:177px;top:198px;width:343px;height:540px}
  .pouch-back{left:696px;top:207px;width:350px;height:510px}

  .stripes{position:absolute;left:0;right:0;top:34px}
  .stripes span{display:block;height:3px;background:var(--brown-mid);margin-bottom:4px}

  /* front */
  .front-art{position:absolute;left:0;top:0}
  .brand-name{position:absolute;left:24px;top:66px;font-family:"Bitter",serif;font-weight:600;font-size:34px;color:var(--brown);margin:0}
  .claim{position:absolute;left:82px;top:112px;font-family:"Bitter",serif;font-weight:800;font-size:16px;color:var(--brown)}
  .product-name{position:absolute;left:22px;top:232px;margin:0;font-family:"Bitter",serif;font-weight:800;font-size:37px;color:var(--gold);text-shadow:2px 2px 0 var(--brown)}
  .product-sub{position:absolute;left:120px;top:283px;font-family:"Bitter",serif;font-weight:800;font-size:13px;color:var(--brown);letter-spacing:.5px}
  .tagline{position:absolute;left:214px;top:390px;transform:rotate(-24deg);transform-origin:left top;font-family:"Bitter",serif;font-weight:800;font-size:20px;color:var(--gold);text-shadow:1px 1px 0 var(--brown)}
  .net-weight{position:absolute;left:236px;top:500px;font-size:10px;line-height:13px;color:var(--paper)}

  /* back */
  .export-corner{position:absolute;right:-42px;top:14px;width:150px;transform:rotate(40deg);background:var(--gold);color:var(--brown);font-weight:700;font-size:10px;text-align:center;padding:4px 0;letter-spacing:1px}
  .ingredients{position:absolute;left:28px;top:70px;font-weight:700;font-size:14px;line-height:18px;color:var(--cream)}
  .nutrition{position:absolute;left:14px;top:120px;width:156px;background:var(--paper);border-radius:8px;padding:6px 7px;box-sizing:border-box;font-size:6.3px;line-height:8px;color:var(--ink)}
  .nutrition h3{margin:0 0 2px;text-align:center;font-size:9px;line-height:10px}
  .nutrition .row{display:flex;justify-content:space-between;border-top:.5px solid #777}
  .nutrition .thick{border-top:2px solid #222}
  .nutrition .ind{padding-left:6px}
  .nutrition p{margin:2px 0}
  .nutrition table{width:100%;border-collapse:collapse;font-size:6px}
  .nutrition td{padding:0}
  .side-note{position:absolute;left:188px;top:130px;writing-mode:vertical-rl;font-size:7px;color:var(--brown);letter-spacing:.5px}
  .side-note.right{left:206px;top:300px}
  .benefits{position:absolute;left:218px;top:148px;margin:0;padding:0;list-style:none}
  .benefits li{display:flex;align-items:center;height:19px;margin-bottom:8px;font-size:9px;color:var(--paper)}
  .benefits svg{margin-right:6px}
  .benefits span{display:block;width:82px;padding:3px 7px;background:linear-gradient(90deg,var(--gold),rgba(246,178,27,.2));border-radius:2px}
  .gmp-mark{position:absolute;left:-6px;top:432px;width:46px;height:46px;border-radius:50%;background:var(--gmp);border:2px solid var(--paper)}
  .packer{position:absolute;left:60px;top:436px;width:150px;font-size:6px;line-height:7.6px;color:var(--paper)}
  .mango-back{position:absolute;right:0;bottom:0}
</style>
</head>
<body>

<section class="pouch pouch-front">
  <svg class="front-art" width="343" height="540" viewBox="0 0 343 540">
    <defs>
      <linearGradient id="slateBand" x1="0" y1="0" x2="1" y2="1">
        <stop offset="0" stop-color="#5a5855"/><stop offset="1" stop-color="#353432"/>
      </linearGradient>
    </defs>
    <polygon points="343,70 343,255 40,440 0,440 0,395 200,140" fill="url(#slateBand)"/>
    <circle cx="42" cy="162" r="25" fill="var(--badge)"/>
    <circle cx="42" cy="162" r="18" fill="var(--gold)"/>
  </svg>
  <div class="stripes"><span></span><span></span><span></span></div>
  <h1 class="brand-name">Orchard nibble</h1>
  <div class="claim">100% Natural</div>
  <h2 class="product-name">Dried Mango</h2>
  <div class="product-sub">EXTRA LOW SUGAR</div>
  <svg class="front-art" width="343" height="540" viewBox="0 0 343 540" role="img" aria-label="Photo of cubed yellow mango pieces">
    <defs>
      <linearGradient id="mangoFront" x1="0" y1="0" x2="1" y2="1">
        <stop offset="0" stop-color="#f7c23a"/><stop offset="1" stop-color="#e48a10"/>
      </linearGradient>
    </defs>
    <polygon points="0,410 90,380 250,395 270,470 230,540 0,540" fill="url(#mangoFront)"/>
  </svg>
  <div class="tagline">Healthy Snack</div>
  <div class="net-weight">Net Wt.: 3.5oz<br>Product of Thailand</div>
</section>

<section class="pouch pouch-back">
  <div class="stripes"><span></span><span></span><span></span></div>
  <div class="export-corner">EXPORT QUALITY</div>
  <div class="ingredients">Ingredients: 100% Mango<br>Store in a container after opening.</div>

  <div class="nutrition">
    <h3>Nutrition Facts</h3>
    <div>Serving Size: 100g</div>
    <div>Serving per Package: 1</div>
    <div class="row thick"><span>Amount per Serving</span></div>
    <div class="row"><span><b>Calories</b> 314</span><span>Calories from Fat 7</span></div>
    <div class="row" style="justify-content:flex-end"><span>% Daily Value*</span></div>
    <div class="row"><span><b>Total Fat</b> 0.78g</span><span>1%</span></div>
    <div class="row ind"><span>Saturated Fat 0.192g</span><span>1%</span></div>
    <div class="row ind"><span>Trans Fat 0g</span><span></span></div>
    <div class="row"><span><b>Cholesterol</b> 0mg</span><span>0%</span></div>
    <div class="row"><span><b>Sodium</b> 6mg</span><span>0%</span></div>
    <div class="row"><span><b>Total Carbohydrate</b> 81.61g</span><span>27%</span></div>
    <div class="row ind"><span>Dietary Fiber 5.2g</span><span>21%</span></div>
    <div class="row ind"><span>Sugars 73.2g</span><span></span></div>
    <div class="row"><span><b>Protein</b> 1.48g</span><span></span></div>
    <div class="row thick"><span>Vitamin A 0%</span><span>Vitamin C 27%</span></div>
    <div class="row"><span>Calcium 1%</span><span>Iron 2%</span></div>
    <p class="row">*Percent Daily Values are based on a 2,000 calorie diet. Your daily values may be higher or lower depending on your calorie needs.</p>
    <table>
      <tr><td></td><td>Calories</td><td>2,000</td><td>2,500</td></tr>
      <tr><td>Total Fat</td><td>Less than</td><td>65g</td><td>80g</td></tr>
      <tr><td>Saturated Fat</td><td>Less than</td><td>20g</td><td>25g</td></tr>
      <tr><td>Cholesterol</td><td>Less than</td><td>300mg</td><td>300mg</td></tr>
      <tr><td>Sodium</td><td>Less than</td><td>2,400mg</td><td>2,400mg</td></tr>
      <tr><td>Total Carbohydrate</td><td></td><td>300g</td><td>375g</td></tr>
      <tr><td>Dietary Fiber</td><td></td><td>25g</td><td>30g</td></tr>
    </table>
    <p>Calories per gram: Fat 9 • Carbohydrate 4 • Protein 4</p>
  </div>

  <div class="side-note">Keep in a cool dry place away from sunlight</div>
  <div class="side-note right">Best before date shown on seal</div>

  <ul class="benefits">
    <li><svg width="10" height="10" viewBox="0 0 10 10"><path d="M1 5 L4 8 L9 1" stroke="#fff" stroke-width="2" fill="none"/></svg><span>Gluten Free</span></li>
    <li><svg width="10" height="10" viewBox="0 0 10 10"><path d="M1 5 L4 8 L9 1" stroke="#fff" stroke-width="2" fill="none"/></svg><span>100% Natural</span></li>
    <li><svg width="10" height="10" viewBox="0 0 10 10"><path d="M1 5 L4 8 L9 1" stroke="#fff" stroke-width="2" fill="none"/></svg><span>No Trans Fat</span></li>
    <li><svg width="10" height="10" viewBox="0 0 10 10"><path d="M1 5 L4 8 L9 1" stroke="#fff" stroke-width="2" fill="none"/></svg><span>No Msg</span></li>
    <li><svg width="10" height="10" viewBox="0 0 10 10"><path d="M1 5 L4 8 L9 1" stroke="#fff" stroke-width="2" fill="none"/></svg><span>No GMOs</span></li>
    <li><svg width="10" height="10" viewBox="0 0 10 10"><path d="M1 5 L4 8 L9 1" stroke="#fff" stroke-width="2" fill="none"/></svg><span>No Cholesterol</span></li>
  </ul>

  <svg class="mango-back" width="130" height="190" viewBox="0 0 130 190" role="img" aria-label="Photo of a halved mango cut into cubes">
    <defs>
      <radialGradient id="mangoBack" cx=".5" cy=".45" r=".6">
        <stop offset="0" stop-color="#f6b52a"/><stop offset=".75" stop-color="#d97a10"/><stop offset="1" stop-color="#5a3214"/>
      </radialGradient>
    </defs>
    <path d="M20 20 Q90 0 130 30 L130 190 L10 190 Q-5 100 20 20 Z" fill="url(#mangoBack)"/>
  </svg>

  <div class="gmp-mark"></div>
  <div class="packer">Packing and Export by:<br>Lotus Trade Supply Co., Ltd.<br>9 Harbor Tower 12th Floor, Unit 1204, River Road, Bang Rak, Bangkok, 10500 THAILAND<br>Tel: (+66) 20004512<br>Mobile: (+66) 810004477, (+66) 820006633</div>
</section>

</body>
</html>
```